Acoustic Jazz album needs cover design

The CD cover has five parts, each one has obligatory features:

I. Main cover

Title: Serenities: Gladness Chants
Artist: Veron Tisdale
Design image*

The main design motive should be something that suggests: happiness, freedom, health, balance, something like that. Please see my other covers at lumevora.com/music. Please don’t use the same key elements as there.
I prefer zen-like, minimalist solutions.
NO stock images, please! Except for unrecognizable parts of something.

II. Cover inside

Track list (10 songs) with durations
All songs written by Veron Tisdale
Copyright Lumevora 2016.
Design image

III. Disc

Artist: Veron Tisdale
All songs written by Veron Tisdale (round on the edge)
Copyright Lumevora 2016. (round on the edge)
www.lumevora.com (round on the edge)

IV. Cover back

Track list (same as cover inside)
Copyright Lumevora 2016.
www.lumevora.com
design image (optional)
The paper of this page is longer than the main cover, because it is to be turned up when put in the CD case, and there is the saddle/spine with the name of the Artist and Title of the album. On both ends.

V. Under the disc

No words, only some design feature.

Important:
The main cover I need in RGB and also CMYK, all the others only CMYK.
I need the work file (cdr, ai or whatever you use)
I need the CMYK images prepared for printing (sizes set, and that little extra on the edges).
I need the RGB main cover cover in jpeg, 3000x3000 pixels.
That's all. :)

The most important of these all is of course the main cover RGB. Make this one first!

Here’s a sample to listen, it might inspire you:

https://www.filebarnex.com/s/72qqtrf41mxbz3c/gladness_chants_medley_veron_tisdale_20160108.mp3?dl=0

And here’s the Veron Tisdale logo:

https://www.filebarnex.com/s/hw3ke82vpnd6ty1/Logo%20VT%20print%2020150216.psd?dl=0

If you take a closer look at my website, you can see the whole concept.

Good luck and enjoy!
Regards,
Veron

Target Market(s)

New age spiritual people

Requirements
Nice to have
• "Simplicity, the ultimate sophistication."
• Don't overdose it with elements. Make it simple.

```html
<!DOCTYPE html>
<html lang="en">
<head>
<meta charset="utf-8">
<title>Serenities: Gladness Chants — Veron Tisdale</title>
<link rel="stylesheet" href="https://fonts.googleapis.com/css2?family=Cormorant+Garamond:wght@500&display=swap">
<style>
  :root {
    --backdrop: #d8d8d8;
    --paper-light: #f4f3ef;
    --paper-dark: #e6e4de;
    --ink-brown: #9a6530;
    --hub-grey: #a9a9a9;
    --hub-grey-dark: #8e8e8e;
    --bloom-red: rgba(222, 40, 40, 0.85);
    --bloom-orange: rgba(238, 150, 80, 0.75);
    --bloom-yellow: rgba(246, 200, 40, 0.75);
    --bloom-teal: rgba(90, 180, 160, 0.7);
    --bloom-violet: rgba(120, 70, 170, 0.6);
  }
  html, body {
    margin: 0;
    width: 1200px;
    height: 749px;
    overflow: hidden;
    background: var(--backdrop);
  }
  .stage {
    position: relative;
    width: 1200px;
    height: 749px;
    font-family: "Cormorant Garamond", Georgia, serif;
    font-weight: 500;
    color: var(--ink-brown);
  }

  /* Front cover */
  .front-cover {
    position: absolute;
    left: 74px;
    top: 107px;
    width: 535px;
    height: 535px;
    overflow: hidden;
    background: linear-gradient(160deg, var(--paper-dark) 0%, var(--paper-light) 45%, var(--paper-dark) 100%);
  }
  .bloom {
    position: absolute;
    border-radius: 50%;
  }
  .front-cover .bloom-corner-top {
    left: -90px;
    top: -90px;
    width: 360px;
    height: 360px;
    background:
      radial-gradient(circle at 45% 45%, var(--bloom-red) 0%, transparent 30%),
      radial-gradient(circle at 25% 25%, var(--bloom-yellow) 0%, transparent 32%),
      radial-gradient(circle at 60% 30%, var(--bloom-teal) 0%, transparent 30%),
      radial-gradient(circle at 60% 62%, var(--bloom-orange) 0%, transparent 28%),
      radial-gradient(circle at 50% 50%, rgba(170, 120, 70, 0.18) 0%, transparent 70%);
  }
  .front-cover .bloom-corner-bottom {
    right: -70px;
    bottom: -70px;
    width: 250px;
    height: 250px;
    background:
      radial-gradient(circle at 45% 35%, var(--bloom-red) 0%, transparent 26%),
      radial-gradient(circle at 55% 55%, var(--bloom-yellow) 0%, transparent 28%),
      radial-gradient(circle at 35% 65%, var(--bloom-teal) 0%, transparent 30%),
      radial-gradient(circle at 60% 40%, var(--bloom-violet) 0%, transparent 24%),
      radial-gradient(circle at 50% 50%, rgba(240, 150, 90, 0.25) 0%, transparent 70%);
  }
  .album-title {
    position: absolute;
    margin: 0;
    text-align: right;
    font-weight: 500;
    line-height: 1;
  }
  .album-title .series {
    display: block;
    letter-spacing: 0.28em;
    margin-right: -0.28em;
    padding-bottom: 3px;
    border-bottom: 1px solid var(--ink-brown);
  }
  .album-title .subtitle {
    display: block;
    padding: 2px 0 4px;
    border-bottom: 1px solid var(--ink-brown);
  }
  .front-cover .album-title {
    right: 22px;
    top: 256px;
  }
  .front-cover .series { font-size: 29px; }
  .front-cover .subtitle { font-size: 37px; }

  .artist-mark {
    position: absolute;
    display: flex;
    align-items: center;
    gap: 8px;
    font-size: 26px;
    color: var(--ink-brown);
  }
  .artist-mark .mark-dot {
    width: 12px;
    height: 12px;
    border-radius: 50%;
    background: var(--ink-brown);
  }
  .front-cover .artist-mark {
    left: 30px;
    top: 460px;
  }

  /* Disc */
  .disc {
    position: absolute;
    left: 653px;
    top: 135px;
    width: 488px;
    height: 488px;
    border-radius: 50%;
    overflow: hidden;
    background: linear-gradient(160deg, var(--paper-light) 0%, #efeee9 60%, var(--paper-dark) 100%);
  }
  .disc .bloom-disc-left {
    left: -70px;
    top: 10px;
    width: 290px;
    height: 290px;
    background:
      radial-gradient(circle at 35% 45%, var(--bloom-red) 0%, transparent 24%),
      radial-gradient(circle at 55% 25%, var(--bloom-yellow) 0%, transparent 22%),
      radial-gradient(circle at 62% 55%, var(--bloom-orange) 0%, transparent 22%),
      radial-gradient(circle at 72% 70%, var(--bloom-teal) 0%, transparent 18%),
      radial-gradient(circle at 50% 50%, rgba(170, 120, 70, 0.18) 0%, transparent 70%);
  }
  .disc .bloom-disc-right {
    right: -60px;
    bottom: -50px;
    width: 300px;
    height: 300px;
    background:
      radial-gradient(circle at 45% 50%, var(--bloom-red) 0%, transparent 22%),
      radial-gradient(circle at 55% 70%, var(--bloom-yellow) 0%, transparent 24%),
      radial-gradient(circle at 35% 72%, var(--bloom-teal) 0%, transparent 24%),
      radial-gradient(circle at 30% 45%, var(--bloom-orange) 0%, transparent 20%),
      radial-gradient(circle at 50% 50%, rgba(170, 120, 70, 0.18) 0%, transparent 70%);
  }
  .disc .album-title {
    right: 78px;
    top: 102px;
  }
  .disc .series { font-size: 15px; }
  .disc .subtitle { font-size: 19px; }
  .disc .artist-mark {
    left: 46px;
    top: 318px;
    font-size: 19px;
    gap: 6px;
  }
  .disc .artist-mark .mark-dot {
    width: 9px;
    height: 9px;
  }
  .disc-hub {
    position: absolute;
    left: 164px;
    top: 164px;
    width: 160px;
    height: 160px;
    border-radius: 50%;
    background: radial-gradient(circle, var(--hub-grey) 55%, var(--hub-grey-dark) 100%);
  }
  .disc-hole {
    position: absolute;
    left: 50px;
    top: 50px;
    width: 60px;
    height: 60px;
    border-radius: 50%;
    background: var(--backdrop);
    box-shadow: 0 0 0 6px #b9b9b9;
  }
</style>
</head>
<body>
<main class="stage">
  <section class="front-cover">
    <div class="bloom bloom-corner-top" role="img" aria-label="Colourful paisley splash with curling golden vines in the top-left corner"></div>
    <div class="bloom bloom-corner-bottom" role="img" aria-label="Colourful paisley splash in the bottom-right corner"></div>
    <h1 class="album-title">
      <span class="series">SERENITIES:</span>
      <span class="subtitle">GLADNESS CHANTS</span>
    </h1>
    <div class="artist-mark"><span class="mark-dot"></span><span>Veron Tisdale</span></div>
  </section>

  <section class="disc">
    <div class="bloom bloom-disc-left" role="img" aria-label="Colourful paisley splash with curling golden vines on the left of the disc"></div>
    <div class="bloom bloom-disc-right" role="img" aria-label="Colourful paisley splash with curling golden vines on the lower right of the disc"></div>
    <h2 class="album-title">
      <span class="series">SERENITIES:</span>
      <span class="subtitle">GLADNESS CHANTS</span>
    </h2>
    <div class="artist-mark"><span class="mark-dot"></span><span>Veron Tisdale</span></div>
    <div class="disc-hub"><div class="disc-hole"></div></div>
  </section>
</main>
</body>
</html>
```